Packaging for Portable Bidet Product

Product:
Our product, Swishka, is a portable hand bidet. What is a portable hand bidet as some may ask? It is small water bottle with a nozzle head that is used to wash “bottoms” after going “poo-poo” (pardon our crudeness). Bidets are popular in European, Asian and African markets and are used alongside toilet paper to give a truly fresh and clean experience. Besides cleanliness, bidets are eco-friendly (they reduce toilet paper usage by x%) and are perfect for travel.
Current Competition + Role of Packaging:
We are launching our portable bidet product in the US market, primarily to be sold via Marketvale. There are currently some existing players in the market, but we’ve done our research and created a product that is superior in functionality and style. That being said, our competitors still have a first-mover advantage and have amassed a high volume of Marketvale ratings, hence we have a bit of a challenge which we feel that can be easily tackled with premium branding and marketing.
That being said, we are looking for a packaging design that:
i. Distinguishing our product on Marketvale (meaning, the packaging looks good in photos)
ii. Highlight that ours is a premium product
Our design values:
‘Hygiene meets modern design’. Some adjectives that describe our brand -
• Clean
• Fresh
• Simple
• Quirky
• Premium
• Discreet
• Subtle
Attachments:
• Our packaging dimensions (see attached)
• Our brand color (Pantone 331C)
• Our logo file (see attached file)
• Product photos (see attached file)
• Illustration of our product instructions (see attached file)
• Packaging designs that inspire us (see attached file)
• Packaging designs of our competition for reference (see attached file)
• Content/text for the packaging box (see below)
What should be on the box:
• Logo and Brand Name
• Product Photo (can be an outline/illustration as well)
• Product instructions illustration (see attached file)
• Text to be included in packaging
o Product description – “A Modern Portable Bidet”
o Bottle size – 400ml
o Key features
Anti-leak
Discreet design
Travel friendly size
Angled spray
Eco-friendly
Easy squeeze bottle
Includes travel bag
Target Market(s)
The product is aimed at both men and women (of all ages) in the US and Canada markets. In terms of audience targets, we will be appealing to outdoor enthusiasts, immigrants abroad, new parents (product to be used to clean their babies), patients (people with limited mobility) and eco-conscious consumers.
Industry/Entity Type
Health And Wellness

```html
<!DOCTYPE html>
<html lang="en">
<head>
<meta charset="utf-8">
<title>Swishka – Portable Bidet Box Dieline</title>
<link rel="stylesheet" href="https://fonts.googleapis.com/css2?family=Montserrat:wght@600;700;800&display=swap">
<style>
  :root {
    --teal-deep: #20748c;
    --teal-mint: #4dc0b4;
    --flap-sage: #80bfb3;
    --mint-light: #a9ddd3;
    --ink-green: #2b5a45;
    --frame-line: #1d3f47;
    --paper: #ffffff;
  }
  html, body {
    margin: 0;
    padding: 0;
    width: 824px;
    height: 1200px;
    overflow: hidden;
    background: var(--paper);
  }
  .dieline {
    display: block;
    width: 824px;
    height: 1200px;
    font-family: "Montserrat", sans-serif;
  }
  .panel-dark { fill: var(--teal-deep); }
  .panel-mint { fill: var(--teal-mint); }
  .flap-bottom { fill: var(--flap-sage); }
  .panel-frame { fill: none; stroke: var(--frame-line); stroke-width: 0.7; }
  .brand-name { fill: var(--mint-light); font-weight: 800; }
  .brand-ring { fill: none; stroke: var(--mint-light); stroke-width: 9; }
  .label-small { fill: var(--ink-green); font-weight: 700; font-size: 4.3px; letter-spacing: 1.2px; }
  .tagline { fill: var(--ink-green); font-weight: 700; font-size: 8px; letter-spacing: 0.3px; }
  .volume { fill: var(--paper); font-weight: 800; font-size: 10px; }
  .features-title { fill: var(--ink-green); font-weight: 800; font-size: 11px; letter-spacing: 3.2px; }
  .feature-item { fill: var(--ink-green); font-weight: 700; font-size: 7px; letter-spacing: 0.2px; }
</style>
</head>
<body>
<svg class="dieline" viewBox="0 0 824 1200" xmlns="http://www.w3.org/2000/svg">
  <defs>
    <linearGradient id="water-tone" x1="0" y1="0" x2="0" y2="1">
      <stop offset="0" stop-color="#cfeaf4"/>
      <stop offset="0.35" stop-color="#6cc6ea"/>
      <stop offset="0.8" stop-color="#1b86c8"/>
      <stop offset="1" stop-color="#bfe2f2"/>
    </linearGradient>
    <linearGradient id="bottle-tone" x1="0" y1="0" x2="0" y2="1">
      <stop offset="0" stop-color="#f1efe9"/>
      <stop offset="0.4" stop-color="#e4e6df"/>
      <stop offset="0.5" stop-color="#a9d8c6"/>
      <stop offset="1" stop-color="#4f8e7c"/>
    </linearGradient>
  </defs>

  <!-- glue flap -->
  <polygon class="panel-dark" points="124,401 66,424 66,794 124,821"/>

  <!-- top flaps -->
  <rect class="panel-dark" x="124" y="255" width="169" height="146"/>
  <polygon class="panel-dark" points="300,320 408,320 440,356 440,401 294,401 300,388"/>
  <polygon class="panel-dark" points="633,323 746,323 746,389 752,401 606,401 606,368"/>

  <!-- lid wordmark, upside down -->
  <g class="lid-brand">
    <text class="brand-name" font-size="26" text-anchor="middle" transform="translate(208,270) rotate(180)">Swishka</text>
    <circle class="brand-ring" cx="208" cy="335" r="36"/>
  </g>

  <!-- main panels: dark upper band -->
  <rect class="panel-dark" x="124" y="401" width="631" height="123"/>
  <!-- main panels: mint lower body -->
  <rect class="panel-mint" x="124" y="524" width="631" height="297"/>

  <!-- band wordmarks -->
  <text class="brand-name" font-size="30" text-anchor="middle" x="208" y="473">Swishka</text>
  <text class="brand-name" font-size="26" text-anchor="middle" x="366" y="471">Swishka</text>
  <text class="brand-name" font-size="30" text-anchor="middle" x="523" y="473">Swishka</text>
  <text class="brand-name" font-size="26" text-anchor="middle" x="681" y="471">Swishka</text>

  <!-- front panel -->
  <g class="panel-front">
    <rect x="126" y="694" width="167" height="127" fill="url(#water-tone)" role="img" aria-label="Splashing water wave illustration"/>
    <rect x="198" y="562" width="76" height="176" rx="30" fill="url(#bottle-tone)" transform="rotate(-20 236 650)" role="img" aria-label="Product photo of the portable bidet bottle with nozzle"/>
    <text class="brand-name" font-size="40" transform="translate(143,540) rotate(90)">Swishka</text>
  </g>

  <!-- description panel -->
  <g class="panel-description">
    <text class="label-small" x="356" y="532">PRODUCT DESCRIPTION</text>
    <text class="brand-name" font-size="27" transform="translate(309,531) rotate(90)">Swishka</text>
    <rect x="322" y="611" width="43" height="189" rx="18" fill="url(#bottle-tone)" role="img" aria-label="Product photo of the bidet bottle standing upright"/>
    <rect x="374" y="536" width="42" height="282" rx="6" fill="#5cc3b6" role="img" aria-label="Five numbered instruction illustrations showing how to fill, attach and use the bidet"/>
  </g>

  <!-- main face panel -->
  <g class="panel-main">
    <rect x="441" y="698" width="164" height="123" fill="url(#water-tone)" role="img" aria-label="Splashing water wave illustration"/>
    <rect x="514" y="564" width="76" height="176" rx="30" fill="url(#bottle-tone)" transform="rotate(-20 552 652)" role="img" aria-label="Product photo of the portable bidet bottle with nozzle"/>
    <text class="brand-name" font-size="40" transform="translate(456,540) rotate(90)">Swishka</text>
    <text class="tagline" x="524" y="793" text-anchor="middle">A MODERN PORTABLE BIDET</text>
    <text class="volume" x="599" y="810" text-anchor="end">400ml</text>
  </g>

  <!-- features panel -->
  <g class="panel-features">
    <text class="features-title" x="681" y="546" text-anchor="middle">KEY FEATURES</text>
    <text class="feature-item" x="682" y="569" text-anchor="middle">ANTI-LEAK</text>
    <text class="feature-item" x="682" y="608" text-anchor="middle">DISCREET DESIGN</text>
    <text class="feature-item" x="682" y="647" text-anchor="middle">TRAVEL FRIENDLY SIZE</text>
    <text class="feature-item" x="682" y="685" text-anchor="middle">ANGLED SPRAY</text>
    <text class="feature-item" x="682" y="724" text-anchor="middle">ECO-FRIENDLY</text>
    <text class="feature-item" x="682" y="763" text-anchor="middle">EASY SQUEEZE BOTTLE</text>
    <text class="feature-item" x="682" y="802" text-anchor="middle">INCLUDES TRAVEL BAG</text>
  </g>

  <!-- panel frames -->
  <rect class="panel-frame" x="126" y="405" width="164" height="416"/>
  <rect class="panel-frame" x="295" y="524" width="140" height="295"/>
  <rect class="panel-frame" x="441" y="405" width="164" height="414"/>
  <rect class="panel-frame" x="612" y="403" width="140" height="416"/>

  <!-- bottom flaps -->
  <polygon class="flap-bottom" points="124,821 293,821 293,940 245,940 242,936 242,894 176,894 176,936 171,940 124,940"/>
  <polygon class="flap-bottom" points="293,821 438,821 438,940 375,940 370,933 370,894"/>
  <polygon class="flap-bottom" points="438,821 606,821 555,894 555,936 550,941 494,941 490,935 490,894"/>
  <polygon class="flap-bottom" points="608,821 755,821 676,894 676,933 671,940 608,940"/>
</svg>
</body>
</html>
```